Design letter head and business card

Hello,

you should design a business card and letter paper for Wolkenfalke Marketing. In German we write this word with K insteat of C.

Company does not have a logo. But in general, we write Wolkenfalke Marketing in 2 lines.
First line red: WOLKENFALKE
Second line gray: MARKETING

Red (or wine red) and Gray / Black are our favorite colors.

Company slogan: "Smart Moves in Online Growth".

Company offers SEO, SEM, SEA, AdWords, Conversion Optimization, Online Markting Consulting ...

The website is old, please do not use this as base for your task.

German letter paper sizes:
Viawable Dimensions : 210 x 297 mm
Needed file dimensions: 212 x 299 mm

Informations to include:

Address:
Wolkenfalke Marketing GmbH
Lindenweg 23
71384 Weinstadt
Germany

Geschäftsführer | CEO: Dietrich Ronnau

Phone: +49 (0) 7151 482 67 05

Fax: +49 (0) 7151 482 67 88

Mail: info@wolkenfalke-marketing.de

Web: www.wolkenfalke-marketing.de

Amtsgericht Suttgart, HRB 736402

Bank: Sonnfelder Bank
IBAN: DE139817325500XXXXXXXX
BIC: GENODES1QTR

Thanks

Dietrich

Target Market(s)

People who likes to win the online marketing game.

Industry/Entity Type

Business

Contact Information for Business Card

Here is the personal text on the card:

Name:
Dietrich Ronnau

Title:
Geschäftsführer | CEO

Address:
Wolkenfalke Marketing GmbH
Lindenweg 23
71384 Weinstadt
Germany

Phone:
+49 (0) 7151 482 67 05

Fax:
+49 (0) 7151 482 67 88

Mail:
ronnau@wolkenfalke-marketing.de

Web:
www.wolkenfalke-marketing.de

Business Card:
Viewable Dimensions: 85 x 55 mm
Needed file dimensions: 87 x 57mm

Font styles to use
Sans Serif

Requirements
Nice to have
• It would be great to see the dynamics of a helicopter.

```html
<!DOCTYPE html>
<html lang="de">
<head>
<meta charset="utf-8">
<title>Wolkenfalke Marketing – Visitenkarte Rückseite</title>
<link rel="stylesheet" href="https://fonts.googleapis.com/css2?family=Saira+Condensed:wght@300;700&display=swap">
<style>
  :root {
    --card-bg: #e6e6e8;
    --ink-dark: #2a2a2c;
    --ink-tag: #3a3a3c;
    --brand-red: #982022;
    --rule-grey: #a6a6a8;
  }
  html, body {
    margin: 0;
    padding: 0;
    width: 1200px;
    height: 667px;
    overflow: hidden;
    background: var(--card-bg);
  }
  .card {
    position: relative;
    width: 1200px;
    height: 667px;
    background: var(--card-bg);
    font-family: "Saira Condensed", "Arial Narrow", sans-serif;
  }
  .brand-dot {
    position: absolute;
    left: 150px;
    top: 100px;
    width: 150px;
    height: 150px;
    border-radius: 50%;
    background: var(--brand-red);
  }
  .brand-name {
    position: absolute;
    left: 68px;
    top: 302px;
    margin: 0;
    font-weight: 700;
    font-size: 63px;
    line-height: 57px;
    letter-spacing: 0;
    color: var(--ink-dark);
    text-transform: uppercase;
  }
  .brand-name span { display: block; }
  .tagline {
    position: absolute;
    left: 70px;
    top: 426px;
    margin: 0;
    font-weight: 300;
    font-size: 34px;
    line-height: 40px;
    color: var(--ink-tag);
  }
  .footer-rule {
    position: absolute;
    left: 72px;
    top: 569px;
    width: 597px;
    height: 2px;
    background: var(--rule-grey);
  }
  .web-address {
    position: absolute;
    left: 689px;
    top: 546px;
    margin: 0;
    font-weight: 700;
    font-size: 36px;
    line-height: 44px;
    color: var(--brand-red);
  }
</style>
</head>
<body>
  <main class="card">
    <div class="brand-dot" aria-hidden="true"></div>
    <h1 class="brand-name"><span>Wolkenfalke</span><span>Marketing</span></h1>
    <p class="tagline">Smart Moves in Online Growth</p>
    <div class="footer-rule" aria-hidden="true"></div>
    <p class="web-address">www.wolkenfalke-marketing.de</p>
  </main>
</body>
</html>
```